Stationary and envelopes

Need to have a new and edgy design for our stationary and matching envelopes. Check out our website at www.quillfordfieldservices.example

We do mainly construction and are the boots on the ground for the energy sector. I had you design our logo now next is stationary to make us stand out? ( boot print)

Target Market(s)

Corporate clients energy company

Font styles to use
Sans Serif

Requirements
Must have
• Logo and energy icons and what we do like the construction management and web address www.quillfordfieldservices.example
• Corporate office
• 48215 county road 92
• Dunmore, co 80999
• 555.614.2873 ( office)
Nice to have
• Logo energy,icons web address corporate office Sterling colorado
• Do not just cut and paste the logo on white paper
Should not have
• Kiddy look imature look

```html
<!DOCTYPE html>
<html lang="en">
<head>
<meta charset="utf-8">
<title>Quillford Field Services Letterhead</title>
<link href="https://fonts.googleapis.com/css2?family=Montserrat:wght@400;500&family=Roboto+Condensed:wght@700&display=swap" rel="stylesheet">
<style>
  :root {
    --backdrop: #dcdcdc;
    --paper: #ffffff;
    --rust: #72231a;
    --navy: #021936;
    --ink: #2b2b2b;
    --boot-grey: #d3d5da;
  }
  * { margin: 0; padding: 0; box-sizing: border-box; }
  html, body { width: 1200px; height: 900px; overflow: hidden; background: var(--backdrop); }
  .letterhead {
    position: absolute; left: 294px; top: 18px;
    width: 612px; height: 864px;
    background: var(--paper); overflow: hidden;
    font-family: "Montserrat", sans-serif;
  }
  .top-band {
    position: absolute; left: 0; top: 0; width: 612px; height: 25px;
    background: var(--rust); border-radius: 0 0 20px 20px;
  }
  .top-tab {
    position: absolute; left: 127px; top: 0; width: 358px; height: 57px;
    background: var(--rust); border-radius: 0 0 32px 32px;
  }
  .services {
    position: absolute; left: 73px; top: 108px; width: 268px; height: 30px;
    background: var(--navy); color: #fff;
    font-family: "Roboto Condensed", sans-serif; font-weight: 700;
    font-size: 11.2px; line-height: 13.5px; text-align: center;
    padding-top: 2px;
  }
  .services .sep { color: #9aa3b2; }
  .brand {
    position: absolute; left: 358px; top: 96px; width: 182px; height: 62px;
    display: flex; align-items: center; justify-content: center; gap: 8px;
  }
  .brand-mark { width: 14px; height: 14px; background: var(--rust); flex: none; }
  .brand-name {
    font-weight: 500; font-size: 16px; line-height: 19px;
    color: var(--rust); letter-spacing: 0.6px; text-transform: uppercase;
  }
  .letter-body {
    position: absolute; left: 73px; top: 232px; width: 467px;
    font-size: 10.5px; line-height: 16.6px; color: var(--ink);
    letter-spacing: 0.15px; text-align: justify; hyphens: auto;
  }
  .letter-body p { text-indent: 31px; margin-bottom: 16.6px; }
  .boot-print {
    position: absolute; left: 59px; top: 658px; width: 147px; height: 126px;
    background: linear-gradient(135deg, var(--boot-grey), #e3e5e8);
    border-radius: 45% 55% 40% 60%;
  }
  .contact {
    position: absolute; left: 318px; top: 685px;
    font-size: 12px; line-height: 16.5px; color: var(--navy);
  }
  .contact li { list-style: none; display: flex; align-items: center; gap: 4px; }
  .contact li.gap { margin-top: 1px; }
  .contact svg { width: 10px; height: 11px; fill: var(--navy); flex: none; }
  .sector-icons {
    position: absolute; left: 177px; top: 806px; display: flex; gap: 22px;
  }
  .sector-icon { width: 24px; height: 36px; background: var(--navy); border-radius: 4px; opacity: 0.9; }
  .foot-corner {
    position: absolute; bottom: 0; width: 127px; height: 33px; background: var(--navy);
  }
  .foot-corner.left { left: 0; border-radius: 0 26px 0 0; }
  .foot-corner.right { right: 0; border-radius: 26px 0 0 0; }
  .foot-line {
    position: absolute; left: 0; bottom: 0; width: 612px; height: 6px; background: var(--navy);
  }
</style>
</head>
<body>
  <main class="letterhead">
    <div class="top-band"></div>
    <div class="top-tab"></div>

    <div class="services">
      INSPECTION <span class="sep">&gt;</span> CONSTRUCTION MANAGEMENT<br>
      TEMPORARY WORKFORCE <span class="sep">&gt;</span> LAND SERVICES
    </div>

    <div class="brand">
      <span class="brand-mark"></span>
      <span class="brand-name">Quillford Field Services</span>
    </div>

    <section class="letter-body">
      <p>Lorem ipsum dolor sit amet, consectetuer adipiscing elit, sed diam nonummy nibh euismod tincidunt ut laoreet dolore magna aliquam erat volutpat. Ut wisi enim ad minim veniam, quis nostrud exerci tation ullamcorper suscipit lobortis nisl ut aliquip ex ea commodo consequat. Duis autem vel eum iriure dolor in hendrerit in vulputate velit esse molestie consequat, vel illum dolore eu feugiat nulla facilisis at vero eros et accumsan et iusto odio dignissim qui blandit praesent luptatum zzril delenit augue duis dolore te feugait nulla facilisi.</p>
      <p>Lorem ipsum dolor sit amet, cons ectetuer adipiscing elit, sed diam nonummy nibh euismod tincidunt ut laoreet dolore magna aliquam erat volutpat. Ut wisi enim ad minim veniam, quis nostrud exerci tation ullamcorper suscipit lobortis nisl ut aliquip ex ea commodo consequat.</p>
      <p>Lorem ipsum dolor sit amet, consectetuer adipiscing elit, sed diam nonummy nibh euismod tincidunt ut laoreet dolore magna aliquam erat volutpat. Ut wisi enim ad minim veniam, quis nostrud exerci tation ullamcorper suscipit lobortis nisl ut aliquip ex ea commodo consequat. Duis autem vel eum iriure dolor in hendrerit in vulputate velit esse molestie consequat, vel illum dolore eu feugiat nulla facilisis at vero eros et accumsan et iusto odio dignissim qui blandit praesent luptatum zzril delenit augue duis dolore te feugait nulla facilisi.</p>
      <p>Lorem ipsum dolor sit amet, cons ectetuer adipiscing elit, sed diam nonummy nibh euismod tincidunt ut laoreet dolore magna aliquam erat volutpat. Ut wisi enim ad minim veniam, quis nostrud exerci tation ullamcorper suscipit lobortis nisl ut aliquip ex ea commodo consequat.</p>
    </section>

    <div class="boot-print" role="img" aria-label="Faint grey boot print tread decoration"></div>

    <ul class="contact">
      <li><svg viewBox="0 0 10 14"><path d="M5 0a5 5 0 0 0-5 5c0 3.5 5 9 5 9s5-5.5 5-9a5 5 0 0 0-5-5zm0 7a2 2 0 1 1 0-4 2 2 0 0 1 0 4z"/></svg>48215 county road 92</li>
      <li>Dunmore, co 80999</li>
      <li class="gap"><svg viewBox="0 0 12 12"><path d="M2.4 0.5l2 2.3-1.1 1.5c.7 1.6 2 2.9 3.6 3.6l1.5-1.1 2.3 2-1.3 2.1C5 10.8 1.2 7 .3 1.8z"/></svg>555.614.2873</li>
      <li class="gap"><svg viewBox="0 0 12 12"><circle cx="6" cy="6" r="5.5"/><path d="M1 6h10M6 .5c2 2.5 2 8.5 0 11M6 .5c-2 2.5-2 8.5 0 11" stroke="#fff" stroke-width="0.8" fill="none"/></svg>www.quillfordfieldservices.example</li>
    </ul>

    <div class="sector-icons">
      <div class="sector-icon" role="img" aria-label="Natural gas flame icon"></div>
      <div class="sector-icon" role="img" aria-label="Transmission tower icon"></div>
      <div class="sector-icon" role="img" aria-label="Oil storage tank icon"></div>
      <div class="sector-icon" role="img" aria-label="Wind turbine icon"></div>
      <div class="sector-icon" role="img" aria-label="Solar panel icon"></div>
      <div class="sector-icon" role="img" aria-label="Survey tripod icon"></div>
    </div>

    <div class="foot-line"></div>
    <div class="foot-corner left"></div>
    <div class="foot-corner right"></div>
  </main>
</body>
</html>
```